Word Studio Lindqvara Templates

We run a large number of businesses, including schools, airports, hotels and offices. We write reports on a daily basis and are looking for a strong and sexy WORD Template. We already have a logo in place (see graphical chart attached), that is rights' protected. We are looking for a beautiful wich reflect modern design and human aspects. Our logo has 2 design, full fill and watermark. It can be used in red or black.

Target Market(s)

Architects, Fire brigade, Building investors, contactors

Font styles to use
Other font styles liked:
• Arial, Calibri, ...

Requirements
Must have
• Cover page, summary, Bullet points, Tables, Figures, Annex

```html
<!DOCTYPE html>
<html lang="en">
<head>
<meta charset="utf-8">
<title>Studio Lindqvara – Report Template Pages</title>
<link href="https://fonts.googleapis.com/css2?family=Montserrat:wght@500;600&family=Roboto+Condensed:wght@400;700&family=Open+Sans:wght@400;600;700&display=swap" rel="stylesheet">
<style>
:root{
  --red:#e3262b;
  --ink:#1b1b1b;
  --grey:#ececec;
  --pink:#fdeeee;
  --board:#e9e9e9;
  --text:#444;
}
*{box-sizing:border-box;margin:0;padding:0}
html,body{width:826px;height:1200px;overflow:hidden;background:var(--board)}
body{position:relative;font-family:"Open Sans",Arial,sans-serif;color:var(--text)}
.page{position:absolute;width:246px;height:347px;background:#fff;overflow:hidden;box-shadow:0 6px 10px rgba(0,0,0,.22)}
.page-label{position:absolute;width:246px;text-align:center;font-family:"Montserrat",sans-serif;font-weight:500;font-size:11.5px;letter-spacing:.5px;color:#333}
.abs{position:absolute}
.footer{position:absolute;left:0;right:0;bottom:0;height:20px;border-top:2px solid var(--red);background:var(--ink);color:#fff;font-size:3.2px;display:flex;align-items:center;justify-content:space-between;padding:0 10px}
.footer .brand{font-family:"Montserrat",sans-serif;font-size:4.4px;line-height:1;text-align:left}
.heading{position:absolute;left:10px;font-family:"Roboto Condensed",sans-serif;font-size:13px;color:var(--red);line-height:1}
.heading b{color:var(--ink);font-weight:400}
.copy{position:absolute;font-size:3.3px;line-height:1.5;color:#555}
.just{text-align:justify}
.label{font-family:"Open Sans",sans-serif;font-weight:700;font-size:3.8px;color:var(--ink)}
.label span{color:var(--red)}
.bullets{list-style:none}
.bullets li{position:relative;padding-left:5px;margin-bottom:5.5px}
.bullets li::before{content:"";position:absolute;left:0;top:1.6px;width:1.6px;height:1.6px;border-radius:50%;background:var(--red)}
.photo{position:absolute}
.stat{position:absolute;top:160px;height:78px;background:var(--grey);text-align:center;color:var(--ink)}
.stat .num{font-family:"Open Sans",sans-serif;font-weight:700;font-size:11px;margin-top:6px}
.stat .cap{font-size:3px;margin-top:4px}
.stat.hot{background:var(--red);color:#fff}
.row-box{position:absolute;height:9px;font-size:3.2px;line-height:9px;padding-left:4px;color:#555}
.tbl{position:absolute;left:10px;width:225px}
.tbl .r{height:10.5px;display:flex;justify-content:space-between;align-items:center;font-size:3.1px;padding:0 4px;color:#555}
.tbl .r:nth-child(odd){background:var(--pink)}
.tbl .btn{margin-left:auto;width:38px;height:8px;background:var(--red);color:#fff;font-size:3px;text-align:center;line-height:8px}
.callout{position:absolute;left:10px;top:265px;width:225px;height:42px;background:var(--ink);color:#fff;display:flex;align-items:center}
.callout-title{flex:none;width:74px;text-align:center;font-family:"Roboto Condensed",sans-serif;line-height:1.2;border-right:1px solid #fff;font-size:4.8px;white-space:nowrap;padding:2px 0}
.callout-title strong{display:block;font-size:8px;font-weight:700}
.callout p{flex:1;font-size:3.2px;line-height:1.5;padding:0 7px;text-align:justify}
.logo-mark{position:absolute;left:646px;top:958px;font-family:"Montserrat",sans-serif;font-weight:500;font-size:20px;line-height:1.05;color:#222;display:flex;align-items:center;gap:8px}
.logo-mark i{display:block;width:14px;height:14px;border-radius:50%;background:var(--red)}
</style>
</head>
<body>

<!-- PAGE 01 : cover -->
<section class="page" style="left:22px;top:29px">
  <svg class="abs" width="246" height="347" viewBox="0 0 246 347">
    <defs>
      <linearGradient id="night" x1="0" y1="0" x2="0" y2="1"><stop offset="0" stop-color="#5a4a36"/><stop offset=".5" stop-color="#2c2a24"/><stop offset="1" stop-color="#1d1e22"/></linearGradient>
      <linearGradient id="warm" x1="0" y1="0" x2="1" y2="1"><stop offset="0" stop-color="#c9b9a6"/><stop offset="1" stop-color="#6c6a66"/></linearGradient>
    </defs>
    <rect x="0" y="0" width="130" height="92" fill="var(--red)"/>
    <path d="M120 0 H246 V240 C200 250 150 225 125 190 C95 145 95 60 120 0 Z" fill="url(#night)" role="img" aria-label="Photo of an illuminated historic hotel facade with palm trees at night"/>
    <path d="M246 243 C200 253 148 228 122 192 C91 146 91 58 116 0" fill="none" stroke="var(--ink)" stroke-width="6"/>
    <circle cx="84" cy="102" r="44" fill="#fff"/>
    <circle cx="84" cy="102" r="40" fill="url(#warm)" role="img" aria-label="Photo of a man working on a laptop"/>
    <circle cx="84" cy="102" r="42" fill="none" stroke="var(--ink)" stroke-width="2"/>
    <circle cx="140" cy="207" r="17" fill="var(--red)"/>
    <circle cx="210" cy="244" r="9" fill="var(--red)" stroke="#fff" stroke-width="1.5"/>
    <g fill="none" stroke="var(--red)" stroke-width=".9">
      <path id="star" d="M16 205 l1.7 3.6 3.9 .5 -2.9 2.7 .8 3.9 -3.5 -1.9 -3.5 1.9 .8 -3.9 -2.9 -2.7 3.9 -.5z"/>
      <use href="#star" x="17"/><use href="#star" x="34"/><use href="#star" x="51"/><use href="#star" x="68"/>
    </g>
    <rect x="11" y="305" width="48" height="2.5" fill="var(--red)"/>
  </svg>
  <div class="abs" style="left:29px;top:14px;font-family:Montserrat,sans-serif;font-weight:500;font-size:10px;line-height:1.1;color:#fff">Studio<br>Lindqvara</div>
  <h1 class="abs" style="left:11px;top:228px;font-family:'Roboto Condensed',sans-serif;font-weight:700;font-size:22.5px;line-height:1.17;color:var(--ink)">Welcome to<br><span style="color:var(--red)">Lorem Ipsum</span> Text<br>Goes Here</h1>
  <div class="footer" style="height:18px"></div>
</section>
<div class="page-label" style="left:22px;top:386px">PAGE - 01</div>

<!-- PAGE 02 -->
<section class="page" style="left:289px;top:29px">
  <svg class="abs" width="246" height="120" viewBox="0 0 246 120">
    <path d="M0 0 H246 V40 C200 90 90 100 0 66 Z" fill="#6a7a8c" role="img" aria-label="Photo of a designer's desk with hands drawing and a coffee mug"/>
    <path d="M0 68 C90 102 200 92 246 42" fill="none" stroke="var(--ink)" stroke-width="6"/>
    <circle cx="111" cy="79" r="14" fill="var(--red)" stroke="#fff" stroke-width="1.5"/>
    <circle cx="209" cy="45" r="8" fill="var(--red)" stroke="#fff" stroke-width="1.5"/>
  </svg>
  <h2 class="heading" style="top:105px">Heading <b>One</b></h2>
  <p class="copy just" style="left:10px;top:123px;width:225px">Lorem Ipsum is simply dummy text of the printing and typesetting industry. Lorem Ipsum has been the industry's standard dummy text ever since the 1500s, when an unknown printer took a galley of type and scrambled it to make a type specimen book. It has survived not only five centuries, but also the leap into electronic typesetting, remaining essentially unchanged. It was popularised in the 1960s with the release of Letraset sheets containing Lorem Ipsum passages.</p>
  <div class="stat" style="left:10px;width:68px"><svg width="14" height="14" viewBox="0 0 14 14" style="margin-top:12px"><rect x="2" y="2" width="10" height="6" fill="none" stroke="#222" stroke-width="1.2"/><path d="M7 8v4M4 12h6" stroke="#222" stroke-width="1.2"/></svg><div class="num">301</div><div class="cap">Lorem Ipsum is simply dummy text.</div></div>
  <div class="stat hot" style="left:83px;width:80px;top:157px;height:81px"><svg width="14" height="14" viewBox="0 0 14 14" style="margin-top:14px"><rect x="1.5" y="2" width="11" height="7" fill="none" stroke="#fff" stroke-width="1.2"/><path d="M7 9v3M4 12h6" stroke="#fff" stroke-width="1.2"/></svg><div class="num">500</div><div class="cap">Lorem Ipsum is simply dummy text.</div></div>
  <div class="stat" style="left:168px;width:67px"><svg width="14" height="14" viewBox="0 0 14 14" style="margin-top:12px"><rect x="2" y="1" width="8" height="12" fill="none" stroke="#222" stroke-width="1.2"/><path d="M4 4h4M4 7h4M4 10h4M10 8h3v5h-3" stroke="#222" stroke-width="1"/></svg><div class="num">201</div><div class="cap">Lorem Ipsum is simply dummy text.</div></div>
  <div class="abs label" style="left:10px;top:258px">TITLE <span>GOES HERE</span></div>
  <ul class="copy bullets" style="left:10px;top:268px;width:110px">
    <li>Lorem Ipsum is simply dummy text of the printing.</li><li>Lorem Ipsum is simply dummy text of the printing.</li><li>Lorem Ipsum is simply dummy text of the printing.</li><li>Lorem Ipsum is simply dummy text of the printing.</li>
  </ul>
  <div class="abs label" style="left:142px;top:258px">TITLE <span>GOES HERE</span></div>
  <p class="copy just" style="left:142px;top:266px;width:93px">Lorem Ipsum is simply dummy text of the printing and typesetting industry. Lorem Ipsum has been the industry's standard dummy text ever since the 1500s.</p>
  <div class="abs label" style="left:142px;top:290px">TITLE <span>GOES HERE</span></div>
  <p class="copy just" style="left:142px;top:298px;width:93px">Lorem Ipsum is simply dummy text of the printing and typesetting industry.</p>
  <div class="footer"><span>www.lindqvara.net</span><span class="brand">Studio<br>Lindqvara</span><span>2</span></div>
</section>
<div class="page-label" style="left:289px;top:386px">PAGE - 02</div>

<!-- PAGE 03 -->
<section class="page" style="left:557px;top:29px">
  <h2 class="heading" style="top:19px">Heading <b>Two</b></h2>
  <p class="copy just" style="left:11px;top:37px;width:224px">Lorem Ipsum is simply dummy text of the printing and typesetting industry. Lorem Ipsum has been the industry's standard dummy text ever since the 1500s, when an unknown printer took a galley of type and scrambled it to make a type specimen book. It has survived not only five centuries, but also the leap into electronic typesetting, remaining essentially unchanged. It was popularised in the 1960s with the release of Letraset sheets containing Lorem Ipsum passages.</p>
  <p class="copy just" style="left:11px;top:63px;width:224px">Lorem Ipsum is simply dummy text of the printing and typesetting industry. Lorem Ipsum has been the industry's standard dummy text ever since the 1500s, when an unknown printer took a galley of type and scrambled it to make a type specimen book. It has survived not only five centuries, but also the leap into electronic typesetting.</p>
  <div class="abs label" style="left:11px;top:94px">TITLE <span>GOES HERE</span></div>
  <ul class="copy bullets" style="left:11px;top:105px;width:224px">
    <li>Lorem Ipsum is simply dummy text of the printing and typesetting industry. Lorem Ipsum has been the industry's standard dummy text ever since the 1500s, when an unknown printer took a galley of type.</li>
    <li>Lorem Ipsum is simply dummy text of the printing and typesetting industry. Lorem Ipsum has been the industry's standard dummy text ever since the 1500s, when an unknown printer took a galley.</li>
  </ul>
  <div class="photo" style="left:11px;top:149px;width:224px;height:69px;background:linear-gradient(120deg,#8a5a3c,#c59a72 50%,#5b4a3f)" role="img" aria-label="Photo of a group of smiling schoolchildren"></div>
  <div class="abs" style="left:11px;top:235px;width:224px;display:flex;justify-content:space-between;text-align:center">
    <div style="width:70px"><svg width="11" height="11" viewBox="0 0 14 14"><rect x="2" y="2" width="10" height="6" fill="none" stroke="#222" stroke-width="1.3"/><path d="M7 8v4M4 12h6" stroke="#222" stroke-width="1.3"/></svg><div style="font-size:4px;font-weight:600;color:var(--red);margin:2px 0">Title One</div><div class="copy" style="position:static">Lorem Ipsum is simply dummy text of the printing and typesetting industry.</div></div>
    <div style="width:70px"><svg width="11" height="11" viewBox="0 0 14 14"><rect x="1.5" y="2" width="11" height="7" fill="none" stroke="#222" stroke-width="1.3"/><path d="M7 9v3M4 12h6" stroke="#222" stroke-width="1.3"/></svg><div style="font-size:4px;font-weight:600;color:var(--red);margin:2px 0">Title Two</div><div class="copy" style="position:static">Lorem Ipsum is simply dummy text of the printing and typesetting industry.</div></div>
    <div style="width:70px"><svg width="11" height="11" viewBox="0 0 14 14"><rect x="2" y="1" width="8" height="12" fill="none" stroke="#222" stroke-width="1.2"/><path d="M4 4h4M4 7h4M4 10h4M10 8h3v5h-3" stroke="#222" stroke-width="1"/></svg><div style="font-size:4px;font-weight:600;color:var(--red);margin:2px 0">Title Three</div><div class="copy" style="position:static">Lorem Ipsum is simply dummy text of the printing and typesetting industry.</div></div>
  </div>
  <p class="copy just" style="left:11px;top:289px;width:224px">Lorem Ipsum is simply dummy text of the printing and typesetting industry. Lorem Ipsum has been the industry's standard dummy text ever since the 1500s, when an unknown printer took a galley of type and scrambled it to make a type specimen book. It has survived not only five centuries, but also the leap into electronic typesetting, remaining essentially unchanged. It was popularised in the 1960s with the release of Letraset sheets.</p>
  <div class="footer"><span>www.lindqvara.net</span><span class="brand">Studio<br>Lindqvara</span><span>3</span></div>
</section>
<div class="page-label" style="left:557px;top:386px">PAGE - 03</div>

<!-- PAGE 04 -->
<section class="page" style="left:22px;top:415px">
  <h2 class="heading" style="top:19px">Heading <b>Three</b></h2>
  <p class="copy just" style="left:10px;top:37px;width:225px">Lorem Ipsum is simply dummy text of the printing and typesetting industry. Lorem Ipsum has been the industry's standard dummy text ever since the 1500s, when an unknown printer took a galley of type and scrambled it to make a type specimen book. It has survived not only five centuries, but also the leap into electronic typesetting, remaining essentially unchanged. It was popularised in the 1960s with the release of Letraset sheets containing Lorem Ipsum passages.</p>
  <div class="abs" style="left:10px;top:74px;width:225px;height:39px;background:var(--pink)"></div>
  <p class="copy just" style="left:18px;top:83px;width:209px">Lorem Ipsum is simply dummy text of the printing and typesetting industry. Lorem Ipsum has been the industry's standard dummy text ever since the 1500s, when an unknown printer took a galley of type and scrambled it to make a type specimen book. It has survived not only five centuries, but also the leap into electronic typesetting, remaining essentially unchanged. It was popularised in the 1960s.</p>
  <svg class="abs" style="left:0;top:120px" width="60" height="200" viewBox="0 0 60 200">
    <path d="M23 36 V172" stroke="var(--red)" stroke-width="1.2"/>
    <g fill="#fff" stroke="var(--red)" stroke-width="1.5">
      <circle cx="23" cy="38" r="13"/><circle cx="23" cy="87" r="13"/><circle cx="23" cy="137" r="13"/><circle cx="23" cy="186" r="13"/>
    </g>
    <g fill="none" stroke="#222" stroke-width="1">
      <rect x="18" y="33" width="10" height="6"/><path d="M23 39v4"/>
      <rect x="17" y="82" width="12" height="7"/><path d="M23 89v3"/>
      <rect x="19" y="131" width="7" height="11"/><path d="M21 134h3M21 137h3"/>
      <rect x="18" y="181" width="10" height="6"/><path d="M23 187v4"/>
    </g>
  </svg>
  <div class="abs" style="left:48px;top:134px;width:188px">
    <div class="label">TITLE <span>GOES HERE</span></div>
    <p class="copy" style="position:static;margin-top:2px">Lorem Ipsum is simply dummy text of the printing and typesetting industry. Lorem Ipsum has been the industry's standard dummy text ever since the 1500s, when an unknown printer took a galley of type and scrambled it to make a type specimen book.</p>
  </div>
  <div class="abs" style="left:48px;top:183px;width:188px">
    <div class="label">TITLE <span>GOES HERE</span></div>
    <p class="copy" style="position:static;margin-top:2px">Lorem Ipsum is simply dummy text of the printing and typesetting industry. Lorem Ipsum has been the industry's standard dummy text ever since the 1500s, when an unknown printer took a galley of type and scrambled it to make a type specimen book.</p>
  </div>
  <div class="abs" style="left:48px;top:233px;width:188px">
    <div class="label">TITLE <span>GOES HERE</span></div>
    <p class="copy" style="position:static;margin-top:2px">Lorem Ipsum is simply dummy text of the printing and typesetting industry. Lorem Ipsum has been the industry's standard dummy text ever since the 1500s, when an unknown printer took a galley of type and scrambled it to make a type specimen book.</p>
  </div>
  <div class="abs" style="left:48px;top:282px;width:188px">
    <div class="label">TITLE <span>GOES HERE</span></div>
    <p class="copy" style="position:static;margin-top:2px">Lorem Ipsum is simply dummy text of the printing and typesetting industry. Lorem Ipsum has been the industry's standard dummy text ever since the 1500s, when an unknown printer took a galley of type and scrambled it to make a type specimen book.</p>
  </div>
  <div class="footer"><span>www.lindqvara.net</span><span class="brand">Studio<br>Lindqvara</span><span>4</span></div>
</section>
<div class="page-label" style="left:22px;top:772px">PAGE - 04</div>

<!-- PAGE 05 -->
<section class="page" style="left:289px;top:415px">
  <h2 class="heading" style="top:19px">Heading <b>Four</b></h2>
  <p class="copy just" style="left:10px;top:37px;width:225px">Lorem Ipsum is simply dummy text of the printing and typesetting industry. Lorem Ipsum has been the industry's standard dummy text ever since the 1500s, when an unknown printer took a galley of type and scrambled it to make a type specimen book. It has survived not only five centuries, but also the leap into electronic typesetting, remaining essentially unchanged. It was popularised in the 1960s with the release of Letraset sheets containing Lorem Ipsum passages.</p>
  <div class="row-box" style="left:10px;top:73px;width:105px;background:var(--pink)">Lorem Ipsum is simply dummy text of the typesetting.</div>
  <div class="row-box" style="left:10px;top:85px;width:105px;background:var(--grey)">Lorem Ipsum is simply dummy text of the typesetting.</div>
  <div class="row-box" style="left:10px;top:97px;width:105px;background:var(--pink)">Lorem Ipsum is simply dummy text of the typesetting.</div>
  <div class="row-box" style="left:10px;top:109px;width:105px;background:var(--grey)">Lorem Ipsum is simply dummy text of the typesetting.</div>
  <div class="row-box" style="left:130px;top:73px;width:105px;background:var(--pink)">Lorem Ipsum is simply dummy text of the typesetting.</div>
  <div class="row-box" style="left:130px;top:85px;width:105px;background:var(--grey)">Lorem Ipsum is simply dummy text of the typesetting.</div>
  <div class="row-box" style="left:130px;top:97px;width:105px;background:var(--pink)">Lorem Ipsum is simply dummy text of the typesetting.</div>
  <div class="row-box" style="left:130px;top:109px;width:105px;background:var(--grey)">Lorem Ipsum is simply dummy text of the typesetting.</div>
  <p class="copy just" style="left:10px;top:132px;width:105px">Lorem Ipsum is simply dummy text of the printing typesetting industry. Lorem Ipsum has been the industry's standard dummy text ever since the 1500s, when an unknown printer took a galley of type and scrambled it to make a type specimen book. It has survived not only five centuries, but also the leap into electronic typesetting, remaining essentially unchanged. It was popularised in the 1960s with the release of Letraset sheets containing Lorem Ipsum passages.</p>
  <p class="copy just" style="left:130px;top:132px;width:105px">Lorem Ipsum is simply dummy text of the printing typesetting industry. Lorem Ipsum has been the industry's standard dummy text ever since the 1500s, when an unknown printer took a galley of type and scrambled it to make a type specimen book.</p>
  <svg class="abs" style="left:18px;top:196px" width="110" height="48" viewBox="0 0 110 48">
    <defs><g id="person"><circle cx="3" cy="1.8" r="1.6"/><path d="M0.8 4h4.4v5h-1v4.5h-2.4V9h-1z"/></g></defs>
    <g fill="var(--red)"><use href="#person" x="0"/><use href="#person" x="8"/><use href="#person" x="16"/><use href="#person" x="24"/><use href="#person" x="32"/><use href="#person" x="40"/><use href="#person" x="48"/><use href="#person" x="56"/><use href="#person" x="64"/><use href="#person" x="72"/></g>
    <g fill="var(--ink)" transform="translate(0,16)"><use href="#person" x="0"/><use href="#person" x="8"/><use href="#person" x="16"/><use href="#person" x="24"/><use href="#person" x="32"/><use href="#person" x="40"/><use href="#person" x="48"/><use href="#person" x="56"/><use href="#person" x="64"/></g>
    <g fill="#bbb" transform="translate(0,32)"><use href="#person" x="0"/><use href="#person" x="8"/><use href="#person" x="16"/><use href="#person" x="24"/><use href="#person" x="32"/><use href="#person" x="40"/><use href="#person" x="48"/><use href="#person" x="56"/></g>
    <path d="M86 2 q4 0 4 6 v10 q0 5 4 5 q-4 0 -4 5 v10 q0 6 -4 6" fill="none" stroke="var(--ink)" stroke-width="1"/>
  </svg>
  <svg class="abs" style="left:146px;top:174px" width="80" height="80" viewBox="0 0 80 80">
    <circle cx="40" cy="40" r="30" fill="none" stroke="#ddd" stroke-width="6"/>
    <circle cx="40" cy="40" r="30" fill="none" stroke="var(--red)" stroke-width="6" stroke-dasharray="149 189" transform="rotate(-90 40 40)"/>
    <path d="M40 3 A37 37 0 0 1 77 40" fill="none" stroke="var(--red)" stroke-width="1.5"/>
    <text x="40" y="45" text-anchor="middle" font-family="Open Sans,sans-serif" font-weight="700" font-size="14" fill="var(--ink)">79%</text>
  </svg>
  <div class="callout">
    <div class="callout-title">LOREM IPSUM<strong>TEXT GOES</strong>LOREM IPSUM</div>
    <p>Lorem Ipsum is simply dummy text of the printing and typesetting industry. Lorem Ipsum has been the industry's standard dummy text ever since the 1500s, when an unknown printer took a galley of type and scrambled it to make a type specimen book. It has survived not only five centuries, but also the leap into electronic typesetting, remaining essentially unchanged.</p>
  </div>
  <div class="footer"><span>www.lindqvara.net</span><span class="brand">Studio<br>Lindqvara</span><span>5</span></div>
</section>
<div class="page-label" style="left:289px;top:772px">PAGE - 05</div>

<!-- PAGE 06 -->
<section class="page" style="left:557px;top:415px">
  <h2 class="heading" style="top:19px">Heading <b>Four</b></h2>
  <div class="photo" style="left:11px;top:49px;width:224px;height:69px;background:linear-gradient(90deg,#3b3f44,#8d9196 45%,#cfcfcf 70%,#4f5257)" role="img" aria-label="Photo of people at a bright office reception hall"></div>
  <div class="abs label" style="left:11px;top:140px">TITLE <span>GOES HERE</span></div>
  <div class="tbl" style="left:11px;top:148px;width:224px">
    <div class="r"><span>1. Lorem Ipsum is simply dummy text of the typesetting</span><span>Lorem Ipsum</span></div>
    <div class="r"><span>2. Lorem Ipsum is simply dummy text of the typesetting</span><span>Lorem Ipsum</span></div>
    <div class="r"><span>3. Lorem Ipsum is simply dummy text of the typesetting</span><span>Lorem Ipsum</span></div>
    <div style="display:flex"><div class="btn">Lorem Ipsum</div></div>
  </div>
  <div class="abs label" style="left:11px;top:198px">TITLE <span>GOES HERE</span></div>
  <div class="tbl" style="left:11px;top:206px;width:224px">
    <div class="r"><span>1. Lorem Ipsum is simply dummy text of the typesetting</span><span>Lorem Ipsum</span></div>
    <div class="r"><span>2. Lorem Ipsum is simply dummy text of the typesetting</span><span>Lorem Ipsum</span></div>
    <div class="r"><span>3. Lorem Ipsum is simply dummy text of the typesetting</span><span>Lorem Ipsum</span></div>
    <div style="display:flex"><div class="btn">Lorem Ipsum</div></div>
  </div>
  <div class="abs label" style="left:11px;top:256px">TITLE <span>GOES HERE</span></div>
  <div class="tbl" style="left:11px;top:264px;width:224px">
    <div class="r"><span>1. Lorem Ipsum is simply dummy text of the typesetting</span><span>Lorem Ipsum</span></div>
    <div class="r"><span>2. Lorem Ipsum is simply dummy text of the typesetting</span><span>Lorem Ipsum</span></div>
    <div class="r"><span>3. Lorem Ipsum is simply dummy text of the typesetting</span><span>Lorem Ipsum</span></div>
    <div style="display:flex"><div class="btn">Lorem Ipsum</div></div>
  </div>
  <div class="footer"><span>www.lindqvara.net</span><span class="brand">Studio<br>Lindqvara</span><span>6</span></div>
</section>
<div class="page-label" style="left:557px;top:772px">PAGE - 06</div>

<!-- PAGE 07 -->
<section class="page" style="left:22px;top:803px">
  <h2 class="heading" style="top:19px">Heading <b>Six</b></h2>
  <svg class="abs" style="left:10px;top:43px" width="225" height="44" viewBox="0 0 225 44">
    <g fill="var(--pink)"><rect width="225" height="10"/><rect y="22" width="225" height="10"/></g>
    <g font-family="Open Sans,sans-serif" font-size="3.2" fill="#555">
      <text x="4" y="6.2">Lorem Ipsum is simply dummy text of the printing</text>
      <text x="4" y="17.2">Lorem Ipsum is simply dummy text of the printing</text>
      <text x="4" y="28.2">Lorem Ipsum is simply dummy text of the printing</text>
      <text x="4" y="39.2">Lorem Ipsum is simply dummy text of the printing</text>
    </g>
    <g fill="var(--red)">
      <rect x="116" y="1" width="16" height="8"/><rect x="134" y="1" width="16" height="8"/><rect x="152" y="1" width="16" height="8"/><rect x="170" y="1" width="16" height="8"/><rect x="188" y="1" width="16" height="8"/><rect x="190" y="1" width="35" height="8"/>
      <rect x="116" y="12" width="16" height="8"/><rect x="134" y="12" width="16" height="8"/>
      <rect x="152" y="23" width="16" height="8"/>
      <rect x="170" y="34" width="16" height="8"/><rect x="188" y="34" width="16" height="8"/>
    </g>
    <g font-family="Open Sans,sans-serif" font-size="3" fill="#fff" text-anchor="middle">
      <text x="124" y="6">Text</text><text x="142" y="6">Text</text><text x="160" y="6">Text</text><text x="178" y="6">Text</text><text x="196" y="6">Text</text><text x="212" y="6">Lorem Ipsum Text</text>
      <text x="124" y="17">Text</text><text x="142" y="17">Text</text><text x="160" y="28">Text</text><text x="178" y="39">Text</text><text x="196" y="39">Text</text>
    </g>
  </svg>
  <p class="copy just" style="left:11px;top:103px;width:105px">Lorem Ipsum is simply dummy text of the printing typesetting industry. Lorem Ipsum has been the industry's standard dummy text ever since the 1500s, when an unknown printer took a galley of type and scrambled it to make a type specimen book.</p>
  <p class="copy just" style="left:11px;top:134px;width:105px">It has survived not only five centuries, but also the leap into electronic typesetting, remaining essentially unchanged. It was popularised in the 1960s with the release of Letraset sheets containing Lorem Ipsum passages.</p>
  <p class="copy just" style="left:130px;top:103px;width:105px">Lorem Ipsum is simply dummy text of the printing typesetting industry. Lorem Ipsum has been the industry's standard dummy text ever since the 1500s.</p>
  <div class="abs" style="left:142px;top:125px;width:93px;height:29px;border:1px solid var(--ink);border-radius:2px;padding:3px 5px;font-size:3.6px;line-height:1.45;color:var(--red)">Lorem Ipsum is simply dummy text of the printing and typesetting industry. Lorem Ipsum has been the industry's <b style="color:var(--ink);font-size:5.5px">100%</b></div>
  <svg class="abs" style="left:0;top:170px" width="246" height="150" viewBox="0 0 246 150">
    <path d="M38 19 H160 A26 26 0 0 1 160 71 H20 A26 26 0 0 0 20 123 H223" fill="none" stroke="var(--red)" stroke-width="1"/>
    <g fill="#fff" stroke="var(--red)" stroke-width="1.4">
      <circle cx="38" cy="19" r="11"/><circle cx="223" cy="45" r="11"/><circle cx="38" cy="97" r="11"/>
      <circle cx="146" cy="19" r="3.5"/><circle cx="96" cy="71" r="3.5"/><circle cx="146" cy="123" r="3.5"/><circle cx="228" cy="123" r="5"/>
    </g>
    <g fill="none" stroke="#222" stroke-width="1">
      <rect x="33" y="14" width="10" height="6"/><path d="M38 20v4"/>
      <rect x="217" y="40" width="12" height="7"/><path d="M223 47v3"/>
      <rect x="35" y="91" width="7" height="11"/><path d="M37 94h3M37 97h3"/>
    </g>
    <circle cx="228" cy="123" r="2.3" fill="var(--red)"/>
  </svg>
  <div class="abs" style="left:11px;top:202px;width:90px"><div class="label">TITLE <span>GOES HERE</span></div><p class="copy" style="position:static;margin-top:2px">Lorem Ipsum is simply dummy text of the printing and typesetting industry. Lorem Ipsum has been the industry's standard dummy text ever since the 1500s.</p></div>
  <div class="abs" style="left:124px;top:202px;width:80px;text-align:right"><div class="label">TITLE <span>GOES HERE</span></div><p class="copy" style="position:static;margin-top:2px">Lorem Ipsum is simply dummy text of the printing and typesetting industry. Lorem Ipsum has been the industry's standard dummy text ever since the 1500s.</p></div>
  <div class="abs" style="left:56px;top:256px;width:180px"><div class="label">TITLE <span>GOES HERE</span></div><p class="copy" style="position:static;margin-top:2px">Lorem Ipsum is simply dummy text of the printing and typesetting industry. Lorem Ipsum has been the industry's standard dummy text ever since the 1500s, when an unknown printer took a galley of type and scrambled it to make a type specimen book. It has survived not only five centuries, remaining essentially unchanged.</p></div>
  <div class="footer"><span>www.lindqvara.net</span><span class="brand">Studio<br>Lindqvara</span><span>7</span></div>
</section>
<div class="page-label" style="left:22px;top:1160px">PAGE - 07</div>

<!-- PAGE 08 : back cover -->
<section class="page" style="left:289px;top:803px">
  <svg class="abs" width="246" height="200" viewBox="0 0 246 200">
    <path d="M0 0 H246 V196 H170 C90 196 20 130 0 40 Z" fill="#5d6670" role="img" aria-label="Photo of two business people shaking hands"/>
    <path d="M0 42 C20 132 90 194 170 194 H246" fill="none" stroke="var(--red)" stroke-width="10"/>
    <circle cx="124" cy="146" r="38" fill="#fff"/>
    <circle cx="124" cy="146" r="35" fill="var(--ink)"/>
  </svg>
  <div class="abs" style="left:89px;top:131px;width:70px;text-align:center;color:#fff;font-family:'Open Sans',sans-serif;line-height:1.2">
    <div style="font-size:7.5px;font-weight:600">Contact Us</div>
    <div style="font-size:12px;font-weight:700">44-71-20</div>
  </div>
  <div class="abs" style="left:66px;top:210px;display:flex;align-items:center;gap:7px;font-family:Montserrat,sans-serif;font-weight:500;font-size:15px;line-height:1.05;color:var(--ink)"><i style="display:block;width:12px;height:12px;border-radius:50%;background:var(--red)"></i><span>Studio<br>Lindqvara</span></div>
  <svg class="abs" style="left:103px;top:262px" width="42" height="10" viewBox="0 0 42 10">
    <g fill="var(--red)"><circle cx="5" cy="5" r="4.5"/><circle cx="21" cy="5" r="4.5"/><circle cx="37" cy="5" r="4.5"/></g>
    <g fill="none" stroke="#fff" stroke-width=".8">
      <path d="M5 7.6 C3 5.5 3 4.5 3 4 a2 2 0 0 1 4 0 c0 .5 0 1.5 -2 3.6z"/>
      <path d="M18.6 3.3h4.8v3.4h-4.8zM18.6 3.3l2.4 1.9 2.4-1.9"/>
      <circle cx="37" cy="5" r="2.3"/><path d="M34.7 5h4.6M37 2.7c-1 1.4-1 3.2 0 4.6M37 2.7c1 1.4 1 3.2 0 4.6"/>
    </g>
  </svg>
  <div class="abs" style="left:0;top:280px;width:246px;text-align:center;font-size:5.3px;line-height:1.75;color:#333">Lorem Ipsum is simply dummy text<br>hello@lindqvara-mail.com<br>www.lindqvara-docs.com</div>
  <div class="footer" style="height:18px"></div>
</section>
<div class="page-label" style="left:289px;top:1160px">PAGE - 08</div>

<!-- standalone brand name -->
<div class="logo-mark"><i></i><span>Studio<br>Lindqvara</span></div>

</body>
</html>
```